Mobile Friendly Lead Generation Landing Page

We are a web marketing company that specialized in web lead generation. Recently we have started buying media from mobile devices and we need a mobile interface(landing page) where we can collect user data in an effective manner.

Our current mobile landing page is:
http://www.pathwaylocate.example.com/lp13d/index.aspx?a=true&source=591483
Through this you can see what the steps/questions users need to answer to get matched to a school. We need the design for the whole process.

We are pretty open for design ideas and our goal is to make this mobile optimized landing page have the look and feel of an app...but not an app.
There are several questions in the process but we are open to changing the way they are presented. As in, you can have one question at a time or a few.
The goal is to make this EXTREMELY EASY for users to interact with.

One example that we have liked is:
http://tutorhubnet.example.com/schools/72615-page1.thub (please note that this opens only on mobile devices)

Some of these screenshots are attached.

Our web form looks like this:
http://www.pathwaylocate.example.com/lp88/index.aspx?a=true

```html
<!DOCTYPE html>
<html lang="en">
<head>
<meta charset="utf-8">
<title>Pathway Locate – Select Area of Interest</title>
<link href="https://fonts.googleapis.com/css2?family=Arimo:wght@400;700&display=swap" rel="stylesheet">
<style>
  :root {
    --frame: #000000;
    --sky: #02a3f7;
    --sky-light: #80d0ff;
    --white: #ffffff;
    --ink: #111111;
    --text: #2b2b2b;
    --olive: #9ea653;
    --chip: #dfe06f;
    --divider: #c9c9c9;
    --chevron: #8a8a8a;
  }
  * { box-sizing: border-box; margin: 0; padding: 0; }
  html, body { width: 678px; height: 1200px; overflow: hidden; }
  body {
    background: var(--frame);
    font-family: "Arimo", "Helvetica Neue", Arial, sans-serif;
    padding: 5px;
  }
  .screen {
    width: 668px; height: 1190px;
    background: var(--white);
    display: flex; flex-direction: column;
    overflow: hidden;
  }

  /* Browser chrome */
  .chrome { background: var(--sky); height: 136px; color: var(--white); }
  .status-bar {
    height: 47px; display: flex; align-items: center;
    justify-content: space-between; padding: 0 14px 0 14px;
    font-size: 22px;
  }
  .status-left, .status-right { display: flex; align-items: center; gap: 8px; width: 200px; }
  .status-right { justify-content: flex-end; }
  .signal { display: flex; gap: 3px; }
  .signal i { width: 10px; height: 10px; border-radius: 50%; border: 1.5px solid var(--white); display: block; }
  .signal i.on { background: var(--white); }
  .clock { font-weight: 400; }
  .address-bar {
    margin: 5px 20px 0 20px; height: 60px; border-radius: 10px;
    background: var(--sky-light);
    display: flex; align-items: center; justify-content: center; position: relative;
    font-size: 31px;
  }
  .address-bar .reload { position: absolute; right: 18px; top: 15px; }

  /* Promo banner */
  .promo {
    height: 285px; position: relative;
    background: linear-gradient(100deg, #fbe5e6 0%, #f6eeee 45%, #efeadc 100%);
  }
  .promo-art {
    position: absolute; left: 18px; top: 14px; width: 190px; height: 190px;
    background: radial-gradient(circle at 45% 45%, #f7f4ef 0 30%, #a9ab5e 31% 100%);
    border-radius: 40% 40% 0 0;
    opacity: .9;
  }
  .promo-title {
    position: absolute; right: 52px; top: 48px; text-align: right;
    font-weight: 700; font-size: 43px; line-height: 54px; color: var(--ink);
  }
  .promo-title .accent { color: var(--sky); }
  .promo-band {
    position: absolute; left: 0; right: 0; top: 203px; height: 50px;
    background: var(--olive); color: var(--white);
    display: flex; align-items: center; justify-content: center;
    font-size: 20px; letter-spacing: .2px;
  }

  /* Interest list */
  .section-title {
    height: 89px; background: var(--sky); color: var(--white);
    display: flex; align-items: center; justify-content: center;
    font-size: 32px; letter-spacing: .3px;
  }
  .interest-list { list-style: none; }
  .interest-item {
    height: 92px; position: relative; display: flex; align-items: center;
    padding-left: 28px;
  }
  .interest-item + .interest-item::before {
    content: ""; position: absolute; left: 31px; right: 0; top: 0;
    height: 1px; background: var(--divider);
  }
  .interest-item:last-child { border-bottom: 1px solid var(--divider); }
  .interest-icon {
    width: 63px; height: 63px; border-radius: 10px; background: var(--chip);
    display: flex; align-items: center; justify-content: center;
    color: var(--white);
  }
  .interest-label { margin-left: 19px; font-size: 26px; color: var(--text); flex: 1; }
  .interest-chevron { margin-right: 38px; }
  .abc { font-size: 15px; line-height: 17px; text-align: center; }
  .abc span { display: block; border-top: 1.5px solid var(--white); }

  .fade-strip { height: 35px; background: linear-gradient(90deg, #f6f8e3, #e8f7ef 60%, #daf6f8); }

  /* Browser toolbar */
  .toolbar {
    height: 93px; background: var(--sky);
    display: flex; align-items: center; justify-content: space-around;
  }
</style>
</head>
<body>
<main class="screen">
  <header class="chrome">
    <div class="status-bar">
      <div class="status-left">
        <span class="signal"><i class="on"></i><i class="on"></i><i class="on"></i><i></i><i></i></span>
        <span class="carrier">Lumacell</span>
        <svg width="26" height="20" viewBox="0 0 26 20" fill="none" stroke="#fff" stroke-width="2.6" stroke-linecap="round">
          <path d="M2 7a16 16 0 0 1 22 0"/><path d="M6 11a10 10 0 0 1 14 0"/><circle cx="13" cy="16" r="1.8" fill="#fff" stroke="none"/>
        </svg>
      </div>
      <span class="clock">4:21 PM</span>
      <div class="status-right">
        <span>100%</span>
        <svg width="44" height="20" viewBox="0 0 44 20"><rect x="1" y="1" width="38" height="18" rx="3" fill="none" stroke="#fff" stroke-width="1.6"/><rect x="3.5" y="3.5" width="33" height="13" rx="1.5" fill="#fff"/><rect x="40" y="7" width="3" height="6" rx="1" fill="#fff"/></svg>
      </div>
    </div>
    <div class="address-bar">
      <span>pathwaylocate.example.com</span>
      <svg class="reload" width="30" height="30" viewBox="0 0 30 30" fill="none" stroke="#fff" stroke-width="3" stroke-linecap="round">
        <path d="M24 15a9 9 0 1 1-3-6.7"/><path d="M22 3v6h-6" stroke-linejoin="round"/>
      </svg>
    </div>
  </header>

  <section class="promo">
    <div class="promo-art" role="img" aria-label="Illustration of a graduate in cap and gown holding a magnifying glass"></div>
    <h1 class="promo-title">Complete our<br><span class="accent">3-MINUTE</span> app!</h1>
    <p class="promo-band">GET UP TO $5, 645* PER YEAR IN GRANTS IF YOU QUALIFY</p>
  </section>

  <h2 class="section-title">SELECT AREA OF YOUR INTEREST</h2>

  <ul class="interest-list">
    <li class="interest-item">
      <span class="interest-icon"><svg width="40" height="40" viewBox="0 0 40 40" fill="none" stroke="#fff" stroke-width="1.8" stroke-linejoin="round"><path d="M34 5 19 22l3 3L36 7z"/><path d="M18 24c-4-1-7 2-7 5s-2 4-5 5c6 1 14 0 15-6z"/></svg></span>
      <span class="interest-label">Art &amp; Design</span>
      <svg class="interest-chevron" width="14" height="24" viewBox="0 0 14 24" fill="none" stroke="var(--chevron)" stroke-width="3"><path d="M2 2l10 10L2 22"/></svg>
    </li>
    <li class="interest-item">
      <span class="interest-icon"><svg width="40" height="40" viewBox="0 0 40 40" fill="none" stroke="#fff" stroke-width="1.8"><rect x="5" y="11" width="30" height="22" rx="1"/><path d="M15 11V7h10v4M5 20h30"/><rect x="18" y="18" width="4" height="4"/></svg></span>
      <span class="interest-label">Business</span>
      <svg class="interest-chevron" width="14" height="24" viewBox="0 0 14 24" fill="none" stroke="var(--chevron)" stroke-width="3"><path d="M2 2l10 10L2 22"/></svg>
    </li>
    <li class="interest-item">
      <span class="interest-icon"><svg width="40" height="40" viewBox="0 0 40 40" fill="none" stroke="#fff" stroke-width="1.8" stroke-linejoin="round"><path d="M20 6l8 8-5 5-8-8z"/><path d="M20 16 7 29l3 3 13-13"/><path d="M20 35h14"/></svg></span>
      <span class="interest-label">Criminal Justice</span>
      <svg class="interest-chevron" width="14" height="24" viewBox="0 0 14 24" fill="none" stroke="var(--chevron)" stroke-width="3"><path d="M2 2l10 10L2 22"/></svg>
    </li>
    <li class="interest-item">
      <span class="interest-icon"><span class="abc">ABC<span>1 2 3</span></span></span>
      <span class="interest-label">Education &amp; Teaching</span>
      <svg class="interest-chevron" width="14" height="24" viewBox="0 0 14 24" fill="none" stroke="var(--chevron)" stroke-width="3"><path d="M2 2l10 10L2 22"/></svg>
    </li>
    <li class="interest-item">
      <span class="interest-icon"><svg width="40" height="40" viewBox="0 0 40 40" fill="none" stroke="#fff" stroke-width="1.8" stroke-linecap="round"><circle cx="20" cy="9" r="3"/><path d="M20 3v3M18 12 9 35M22 12l9 23M12 26c5 3 11 3 16 0"/></svg></span>
      <span class="interest-label">Engineering</span>
      <svg class="interest-chevron" width="14" height="24" viewBox="0 0 14 24" fill="none" stroke="var(--chevron)" stroke-width="3"><path d="M2 2l10 10L2 22"/></svg>
    </li>
    <li class="interest-item">
      <span class="interest-icon"><svg width="40" height="40" viewBox="0 0 40 40" fill="none" stroke="#fff" stroke-width="1.8" stroke-linejoin="round"><path d="M20 12c-4-3-9-3-14-2v20c5-1 10-1 14 2 4-3 9-3 14-2V10c-5-1-10-1-14 2zM20 12v20"/></svg></span>
      <span class="interest-label">Other</span>
      <svg class="interest-chevron" width="14" height="24" viewBox="0 0 14 24" fill="none" stroke="var(--chevron)" stroke-width="3"><path d="M2 2l10 10L2 22"/></svg>
    </li>
  </ul>

  <div class="fade-strip"></div>

  <nav class="toolbar">
    <svg width="30" height="44" viewBox="0 0 30 44" fill="none" stroke="#fff" stroke-width="3"><path d="M24 3 6 22l18 19"/></svg>
    <svg width="30" height="44" viewBox="0 0 30 44" fill="none" stroke="#fff" stroke-width="3"><path d="M6 3l18 19L6 41"/></svg>
    <svg width="40" height="48" viewBox="0 0 40 48" fill="none" stroke="#fff" stroke-width="2.4"><path d="M13 16H3v30h34V16H27M20 30V3M12 11l8-8 8 8"/></svg>
    <svg width="52" height="42" viewBox="0 0 52 42" fill="none" stroke="#fff" stroke-width="2.4" stroke-linejoin="round"><path d="M26 8C20 2 10 2 2 4v34c8-2 18-2 24 2 6-4 16-4 24-2V4c-8-2-18-2-24 4zM26 8v32"/></svg>
    <svg width="48" height="48" viewBox="0 0 48 48" fill="none" stroke="#fff" stroke-width="2.4"><rect x="2" y="12" width="34" height="34"/><path d="M12 12V2h34v34H36"/></svg>
  </nav>
</main>
</body>
</html>
```